Design home page for SME Tidewell

WordPress homepage for SME Tidewell.
Will use GeneratePress, and the theme will be a child theme of Generate Press.
Logo attached.
SME Tidewell is a business that advises Small to Medium Businesses towards success.

```html
<!DOCTYPE html>
<html lang="en">
<head>
<meta charset="utf-8">
<title>SME Tidewell – Home</title>
<link href="https://fonts.googleapis.com/css2?family=Marcellus&family=Lato:ital,wght@0,400;0,700;1,400&display=swap" rel="stylesheet">
<style>
:root{
  --blue:#2b5597;
  --blue-dark:#234a86;
  --orange:#f2650f;
  --ink:#222;
  --text:#3a3a3a;
  --muted:#f3f4f7;
  --footer:#0b0b0b;
  --white:#fff;
}
*{box-sizing:border-box;margin:0;padding:0}
html,body{width:1200px;height:4264px;overflow:hidden}
body{font-family:"Lato",sans-serif;color:var(--text);background:var(--white);position:relative}
.serif{font-family:"Marcellus",serif}
section,header,nav,footer{position:relative;width:1200px}
.abs{position:absolute}

/* header */
.topbar{height:70px}
.brand{left:132px;top:14px;display:flex;align-items:center;gap:12px}
.brand-mark{width:38px;height:38px;background:#5d6470}
.brand-name{font-family:"Marcellus",serif;font-size:34px;color:var(--ink);letter-spacing:.5px}
.socials-top{left:708px;top:10px;display:flex;gap:13px}
.circle-o{width:42px;height:42px;border:2px solid var(--orange);border-radius:50%;display:flex;align-items:center;justify-content:center}
.circle-o span{width:14px;height:14px;background:var(--orange);border-radius:3px}
.call{left:872px;top:12px;display:flex;align-items:center;gap:10px}
.call-icon{width:38px;height:38px;border-radius:50%;background:var(--blue);display:flex;align-items:center;justify-content:center}
.call small{display:block;font-size:9px;color:var(--orange);letter-spacing:.3px}
.call strong{display:block;font-family:"Marcellus",serif;font-weight:400;font-size:21px;color:var(--blue)}

/* nav */
.mainnav{height:53px;background:var(--blue)}
.mainnav ul{list-style:none}
.mainnav li{position:absolute;top:0;line-height:53px;font-size:14px;color:var(--white);letter-spacing:.3px}
.mainnav li.active{color:var(--orange)}
.mainnav li.active::after{content:"";position:absolute;left:50%;top:40px;width:5px;height:5px;border-radius:50%;background:var(--white);transform:translateX(-50%)}
.nav-contact{left:907px;width:153px;height:53px;background:var(--orange);text-align:center}

/* hero */
.hero{height:599px;overflow:hidden}
.hero-photo{position:absolute;inset:0;background:linear-gradient(90deg,#3b3f44 0%,#6f7378 45%,#8a8e92 70%,#5a5d60 100%)}
.hero-photo::after{content:"";position:absolute;inset:0;background:rgba(0,0,0,.38)}
.hero-content{position:absolute;left:0;right:0;top:0;text-align:center;color:var(--white)}
.hero-kicker{position:absolute;left:0;right:0;top:175px;font-size:17px;letter-spacing:7px}
.hero-title{position:absolute;left:0;right:0;top:196px;font-family:"Marcellus",serif;font-size:84px;letter-spacing:1px}
.hero-text{position:absolute;left:200px;right:200px;top:290px;font-size:13px;line-height:24px}
.btn{display:inline-block;background:var(--orange);color:var(--white);font-family:"Marcellus",serif;font-size:16px;text-align:center}
.hero .btn{position:absolute;left:526px;top:357px;width:148px;height:45px;line-height:45px}
.dots{display:flex;gap:6px;justify-content:center}
.dots i{width:9px;height:9px;border-radius:50%;background:var(--white)}
.dots i.on{background:var(--orange)}
.hero .dots{position:absolute;left:0;right:0;top:568px}

/* section heading */
.sec-title{position:absolute;left:0;right:0;text-align:center;font-family:"Marcellus",serif;font-size:36px;color:var(--blue)}
.sec-title::after{content:"";display:block;width:36px;height:4px;background:var(--orange);margin:12px auto 0}

/* services */
.services{height:601px;background:var(--muted)}
.card{position:absolute;background:var(--white);border-radius:8px;box-shadow:0 3px 12px rgba(0,0,0,.12);text-align:center}
.svc{top:172px;width:298px;height:323px}
.svc.lift{top:168px;box-shadow:0 8px 20px rgba(0,0,0,.2)}
.svc-icon{width:86px;height:86px;border-radius:50%;background:var(--blue);margin:21px auto 0;display:flex;align-items:center;justify-content:center}
.svc-icon.orange{background:var(--orange)}
.svc h3{font-family:"Marcellus",serif;font-weight:400;font-size:18px;color:var(--blue);margin-top:16px}
.svc h3.orange{color:var(--orange)}
.svc h3::after{content:"";display:block;width:32px;height:3px;background:var(--blue);margin:8px auto 0}
.svc h3.orange::after{background:var(--orange)}
.svc p{font-size:13.5px;line-height:28px;color:var(--ink);padding:4px 18px 0}
.svc a{display:inline-block;margin-top:20px;font-family:"Marcellus",serif;font-size:11px;color:var(--blue);text-decoration:underline}
.svc a.orange{color:var(--orange)}

/* about */
.about{height:541px}
.about p{position:absolute;left:170px;right:170px;top:172px;text-align:center;font-size:13.5px;line-height:28px;color:var(--ink)}
.about .btn{position:absolute;left:526px;top:398px;width:148px;height:45px;line-height:45px}

/* team */
.team{height:540px;background:#f4f4f4}
.ph{position:absolute}
.bio{position:absolute;color:var(--white);padding:16px 34px}
.bio h3{font-family:"Marcellus",serif;font-weight:400;font-size:23px}
.bio p{font-size:13px;line-height:24px;margin-top:6px}
.bio.one{left:343px;top:0;width:508px;height:266px;background:var(--orange);padding-left:26px}
.bio.one p{padding-left:9px;text-align:justify}
.bio.two{left:348px;top:273px;width:503px;height:267px;background:var(--blue);text-align:right}
.bio.two p{text-align:center;padding-left:10px}
.soc{display:flex;gap:9px;margin-top:12px}
.bio.one .soc{padding-left:9px}
.bio.two .soc{justify-content:flex-end}
.soc i{width:36px;height:36px;border-radius:50%;background:var(--white)}

/* testimonials */
.testimonials{height:751px}
.tcard{top:227px;width:300px;height:336px}
.tcard.lift{top:203px;box-shadow:0 8px 20px rgba(0,0,0,.18)}
.avatar{width:86px;height:86px;border-radius:50%;margin:26px auto 0;background:linear-gradient(180deg,#b9bcc2,#3d4858)}
.tcard h4{font-family:"Lato",sans-serif;font-weight:400;font-size:15px;color:var(--ink);margin-top:10px;line-height:24px}
.tcard p{font-style:italic;font-size:13px;line-height:24px;color:var(--ink);padding:6px 22px 0;text-align:justify;text-align-last:center}
.stars{color:var(--orange);font-size:13px;letter-spacing:2px;margin-top:6px}
.arrows{position:absolute;left:521px;top:599px;display:flex;gap:38px}
.arrow{width:60px;height:60px;border-radius:50%;background:var(--white);box-shadow:0 4px 12px rgba(0,0,0,.12);display:flex;align-items:center;justify-content:center}

/* news */
.news{height:548px;background:linear-gradient(180deg,#eceff3,#f6f7f9)}
.news-item{position:absolute;top:175px;width:227px;text-align:center}
.news-img{height:162px;background:linear-gradient(135deg,#aeb3b9,#5f6770)}
.news-item.active .news-img{outline:3px solid var(--orange);outline-offset:-3px}
.news-item h4{font-family:"Marcellus",serif;font-weight:400;font-size:15px;line-height:24px;color:var(--ink);margin-top:16px}
.news .dots{position:absolute;left:0;right:0;top:465px}
.news .dots i{background:#e3e5e9}
.news .dots i.on{background:var(--orange)}

/* footer */
.site-footer{height:561px;background:var(--footer);color:var(--white)}
.site-footer .brand-name{color:var(--white)}
.site-footer .brand-mark{background:#8a8f96}
.subscribe{left:554px;top:65px;display:flex}
.subscribe .field{width:345px;height:50px;border:1px solid #aaa;font-size:12px;line-height:48px;padding-left:24px;color:var(--white)}
.subscribe .btn{width:155px;height:50px;line-height:50px;font-size:15px}
.rule{left:88px;width:1002px;height:1px;background:#555}
.ft-h{font-family:"Marcellus",serif;font-size:20px}
.input{position:absolute;background:var(--white);color:#333;font-size:12px;padding:14px 12px}
.links{list-style:none;font-size:12px;line-height:28px}
.contact-row{display:flex;gap:12px;font-size:12px;line-height:28px}
.contact-row svg{flex:none;margin-top:8px}
.foot-soc{display:flex;gap:16px}
.foot-soc i{width:28px;height:28px;border-radius:50%;background:var(--blue)}
.copy{left:0;right:0;top:500px;text-align:center;font-size:11px}
</style>
</head>
<body>

<header class="topbar">
  <div class="abs brand"><span class="brand-mark"></span><span class="brand-name">SME Tidewell</span></div>
  <div class="abs socials-top" aria-label="Social profiles">
    <div class="circle-o"><span></span></div>
    <div class="circle-o"><span></span></div>
    <div class="circle-o"><span></span></div>
  </div>
  <div class="abs call">
    <div class="call-icon">
      <svg width="18" height="18" viewBox="0 0 24 24"><path fill="#fff" d="M6.6 10.8a15.1 15.1 0 0 0 6.6 6.6l2.2-2.2c.3-.3.7-.4 1-.2 1.1.4 2.3.6 3.6.6.6 0 1 .4 1 1V20c0 .6-.4 1-1 1A17 17 0 0 1 3 4c0-.6.4-1 1-1h3.5c.6 0 1 .4 1 1 0 1.3.2 2.5.6 3.6.1.3 0 .7-.2 1z"/></svg>
    </div>
    <div><small>CALL US TODAY</small><strong>+1 555 010 2040</strong></div>
  </div>
</header>

<nav class="mainnav">
  <ul>
    <li class="active" style="left:187px">HOME</li>
    <li style="left:273px">ABOUT US</li>
    <li style="left:386px">OUR SERVICES</li>
    <li style="left:527px">OUR TEAM</li>
    <li style="left:644px">TESTIMONIALS</li>
    <li style="left:790px">BLOG</li>
    <li class="nav-contact">CONTACT</li>
  </ul>
</nav>

<section class="hero">
  <div class="hero-photo" role="img" aria-label="Photo of a team of professionals walking through a bright open-plan office"></div>
  <div class="hero-content">
    <div class="hero-kicker">WELCOME TO</div>
    <h1 class="hero-title" style="font-weight:400">SME TIDEWELL</h1>
    <p class="hero-text">Lorem ipsum dolor sit amet, consectetur adipiscing elit, sed do eiusmod tempor incididunt ut labore et dolore magna aliqua. Quis ipsum suspendisse ultrices gravida. Risus commodo viverra maecenas accumsan lacus vel facilisis.</p>
    <span class="btn">GET STARTED</span>
    <div class="dots"><i class="on"></i><i></i><i></i><i></i></div>
  </div>
</section>

<section class="services">
  <h2 class="sec-title" style="top:75px;font-weight:400">OUR SERVICES</h2>
  <div class="card svc" style="left:131px">
    <div class="svc-icon"><svg width="44" height="44" viewBox="0 0 24 24" fill="none" stroke="#fff" stroke-width="1.4"><circle cx="9" cy="13" r="4"/><circle cx="16" cy="8" r="3"/></svg></div>
    <h3>LOREM IPSUM DOLOR</h3>
    <p>Lorem ipsum dolor sit amet, consectetur adipiscing elit, sed do eiusmod tempor incididunt ut labore et dolore magna aliqua. Quis ipsum suspendisse .</p>
    <a>LEARN MORE</a>
  </div>
  <div class="card svc lift" style="left:451px">
    <div class="svc-icon orange"><svg width="44" height="44" viewBox="0 0 24 24" fill="none" stroke="#fff" stroke-width="1.4"><path d="M4 18h16M7 15l4-4 3 3 5-6"/></svg></div>
    <h3 class="orange">LOREM IPSUM DOLOR</h3>
    <p>Lorem ipsum dolor sit amet, consectetur adipiscing elit, sed do eiusmod tempor incididunt ut labore et dolore magna aliqua. Quis ipsum suspendisse .</p>
    <a class="orange">LEARN MORE</a>
  </div>
  <div class="card svc" style="left:770px">
    <div class="svc-icon"><svg width="44" height="44" viewBox="0 0 24 24" fill="none" stroke="#fff" stroke-width="1.4"><circle cx="8" cy="15" r="3.5"/><path d="M12 12l3-3 2 2 3-4"/></svg></div>
    <h3>LOREM IPSUM DOLOR</h3>
    <p>Lorem ipsum dolor sit amet, consectetur adipiscing elit, sed do eiusmod tempor incididunt ut labore et dolore magna aliqua. Quis ipsum suspendisse .</p>
    <a>LEARN MORE</a>
  </div>
</section>

<section class="about">
  <h2 class="sec-title" style="top:93px;font-weight:400">ABOUT SME TIDEWELL</h2>
  <p>Lorem ipsum dolor sit amet, consectetur adipiscing elit, sed do eiusmod tempor incididunt ut labore et dolore magna aliqua. Quis ipsum suspendisse ultrices gravida. Risus commodo viverra maecenas accumsan lacus vel facilisis. ut perspiciatis unde omnis iste natus error sit voluptatem accusantium doloremque laudantium, totam rem aperiam, eaque ipsa quae ab illo inventore veritatis et quasi architecto beatae vitae dicta sunt explicabo. Nemo enim ipsam voluptatem quia voluptas sit aspernatur aut odit aut fugit, sed quia consequuntur magni dolores eos qui ratione voluptatem sequi nesciunt. Neque porro quisquam est, qui dolorem ipsum quia dolor sit amet, consectetur, adipisci velit, sed quia non numquam eius modi tempora incidunt ut labore et dolore magnam aliquam quaerat voluptatem. Ut enim ad minima veniam, quis nostrum exercitationem ullam corporis suscipit laboriosam nisi ut aliquid ex ea commodi consequatur.</p>
  <span class="btn">LEARN MORE</span>
</section>

<section class="team">
  <div class="ph" style="left:0;top:0;width:343px;height:540px;background:linear-gradient(180deg,#d8d2c8,#b8b2aa)" role="img" aria-label="Portrait photo of team member Maren in a light blazer"></div>
  <div class="ph" style="left:857px;top:0;width:343px;height:540px;background:linear-gradient(180deg,#cfd6de,#7d93ad)" role="img" aria-label="Portrait photo of team member Tobias in a blue suit holding a tablet"></div>
  <div class="bio one">
    <h3>MAREN</h3>
    <p>Lorem ipsum dolor sit amet, consectetur adipiscing elit, sed do eiusmod tempor incididunt ut labore et dolore magna aliqua. Quis ipsum suspendisse ultrices gravida. Risus commodo viverra maecenas accumsan lacus vel facilisis. Lorem ipsum dolor sit amet, consectetur adipiscing elit, sed do eiusmod tempor incididunt ut labore et dolore magna aliqua. Quis ipsum suspendisse ultrices gravida.</p>
    <div class="soc"><i></i><i></i><i></i><i></i></div>
  </div>
  <div class="bio two">
    <h3>TOBIAS</h3>
    <p>Lorem ipsum dolor sit amet, consectetur adipiscing elit, sed do eiusmod tempor incididunt ut labore et dolore magna aliqua. Quis ipsum suspendisse ultrices gravida. Risus commodo viverra maecenas accumsan lacus vel facilisis. Lorem ipsum dolor sit amet, consectetur adipiscing elit, sed do eiusmod tempor incididunt ut labore et dolore magna aliqua. Quis ipsum suspendisse ultrices gravida.</p>
    <div class="soc"><i></i><i></i><i></i><i></i></div>
  </div>
</section>

<section class="testimonials">
  <h2 class="sec-title" style="top:100px;font-weight:400">OUR CLIENT TESTIMONIALS</h2>
  <div class="card tcard" style="left:126px">
    <div class="avatar" role="img" aria-label="Client portrait"></div>
    <h4>Elliot R.<br>Lorem ipsum dolor sit amet</h4>
    <p>Lorem ipsum dolor sit amet, consectetur adipiscing elit, sed do eiusmod tempor incididunt ut labore et dolore magna aliqua. Quis ipsum suspendisse ultrices gravida. Risus commodo viverra maecenas.</p>
    <div class="stars">★★★★★</div>
  </div>
  <div class="card tcard lift" style="left:451px">
    <div class="avatar" role="img" aria-label="Client portrait"></div>
    <h4>Elliot R.<br>Lorem ipsum dolor sit amet</h4>
    <p>Lorem ipsum dolor sit amet, consectetur adipiscing elit, sed do eiusmod tempor incididunt ut labore et dolore magna aliqua. Quis ipsum suspendisse ultrices gravida. Risus commodo viverra maecenas.</p>
    <div class="stars">★★★★★</div>
  </div>
  <div class="card tcard" style="left:775px">
    <div class="avatar" role="img" aria-label="Client portrait"></div>
    <h4>Elliot R.<br>Lorem ipsum dolor sit amet</h4>
    <p>Lorem ipsum dolor sit amet, consectetur adipiscing elit, sed do eiusmod tempor incididunt ut labore et dolore magna aliqua. Quis ipsum suspendisse ultrices gravida. Risus commodo viverra maecenas.</p>
    <div class="stars">★★★★★</div>
  </div>
  <div class="arrows">
    <div class="arrow"><svg width="20" height="20" viewBox="0 0 24 24" fill="none" stroke="#f2650f" stroke-width="3"><path d="M20 12H5M11 5l-7 7 7 7"/></svg></div>
    <div class="arrow"><svg width="20" height="20" viewBox="0 0 24 24" fill="none" stroke="#f2650f" stroke-width="3"><path d="M4 12h15M13 5l7 7-7 7"/></svg></div>
  </div>
</section>

<section class="news">
  <h2 class="sec-title" style="top:88px;font-weight:400">OUR LATEST NEWS</h2>
  <div class="news-item" style="left:131px"><div class="news-img" role="img" aria-label="Photo of colleagues meeting at an office table"></div><h4>LOREM IPSUM DOLOR SIT AMET CONSECTETUR ADIPISCING.</h4></div>
  <div class="news-item active" style="left:369px"><div class="news-img" role="img" aria-label="Photo of a businessman working at a laptop"></div><h4>LOREM IPSUM DOLOR SIT AMET CONSECTETUR.</h4></div>
  <div class="news-item" style="left:606px"><div class="news-img" role="img" aria-label="Photo of two people reviewing documents"></div><h4>LOREM IPSUM DOLOR SIT AMET CONSECTETUR ADIPISCING.</h4></div>
  <div class="news-item" style="left:843px"><div class="news-img" role="img" aria-label="Photo of a team discussion in a meeting room"></div><h4>LOREM IPSUM DOLOR SIT AMET CONSECTETUR.</h4></div>
  <div class="dots"><i class="on"></i><i></i><i></i><i></i></div>
</section>

<footer class="site-footer">
  <div class="abs brand" style="top:70px"><span class="brand-mark"></span><span class="brand-name">SME Tidewell</span></div>
  <div class="abs subscribe"><div class="field">Enter the email</div><span class="btn">SUBSCRIBE</span></div>
  <div class="abs rule" style="top:148px"></div>

  <div class="abs ft-h" style="left:107px;top:197px">GET IN TOUCH</div>
  <div class="input" style="left:110px;top:240px;width:218px;height:42px">Full Name</div>
  <div class="input" style="left:339px;top:240px;width:220px;height:42px">Phone Number</div>
  <div class="input" style="left:110px;top:296px;width:449px;height:42px">Email address</div>
  <div class="input" style="left:110px;top:352px;width:449px;height:94px">Message</div>
  <svg class="abs" style="left:489px;top:382px" width="70" height="64" viewBox="0 0 70 64"><path d="M70 0V64H0z" fill="#f2650f"/><path d="M42 52l16-9-14 4zm0 0l3-6" stroke="#fff" stroke-width="2" fill="#fff"/></svg>

  <div class="abs ft-h" style="left:592px;top:197px">QUICK LINKS</div>
  <ul class="abs links" style="left:595px;top:233px">
    <li>Home</li><li>About Us</li><li>Our Services</li><li>Our Team</li><li>Testimonials</li><li>Blog</li><li>Contact Us</li>
  </ul>

  <div class="abs ft-h" style="left:793px;top:197px">CONTACT US</div>
  <div class="abs" style="left:796px;top:233px;width:260px">
    <div class="contact-row"><svg width="11" height="13" viewBox="0 0 24 28"><path fill="#fff" d="M12 0a10 10 0 0 0-10 10c0 7 10 18 10 18s10-11 10-18A10 10 0 0 0 12 0zm0 14a4 4 0 1 1 0-8 4 4 0 0 1 0 8z"/></svg><span>123 Lorem ipsum dolor sit amet, consectetur adipiscing elit.</span></div>
    <div class="contact-row" style="margin-top:8px"><svg width="12" height="12" viewBox="0 0 24 24"><path fill="#fff" d="M6.6 10.8a15.1 15.1 0 0 0 6.6 6.6l2.2-2.2c.3-.3.7-.4 1-.2 1.1.4 2.3.6 3.6.6.6 0 1 .4 1 1V20c0 .6-.4 1-1 1A17 17 0 0 1 3 4c0-.6.4-1 1-1h3.5c.6 0 1 .4 1 1 0 1.3.2 2.5.6 3.6.1.3 0 .7-.2 1z"/></svg><span>+1 555 010 2040</span></div>
    <div class="contact-row" style="margin-top:12px"><svg width="13" height="11" viewBox="0 0 24 18"><path fill="#fff" d="M0 0h24v18H0zM2 2l10 7 10-7"/></svg><span>hello@smetidewell.com</span></div>
    <div class="foot-soc" style="margin-top:18px"><i></i><i></i><i></i><i></i></div>
  </div>

  <div class="abs rule" style="top:476px"></div>
  <div class="abs copy">© Copyrights 2022 SME Tidewell &nbsp;|&nbsp;&nbsp; All rights reserved.</div>
</footer>

</body>
</html>
```